Flyer Design Project

My client is looking for a template of a flyer design that we can add content to. Quillstone Realty LLC is a real estate brokerage firm in Nashville, TN that has an unconventional business model: they offer agents 100% commission and low, flat monthly or annual fees in exchange for broker support and use of office equipment. The business has literally doubled in size and revenue the last three years in a row.

The primary audience is passionate real estate professionals, 75% female, 35 - 45 years of age who are advanced, independent and savvy.

Their position is that Quillstone Realty is:

- Selective
- Innovative and Successful
- Exemplar

The brand filters, through which we approach all creative endeavors are as follows. We seek to communicate that Quillstone Realty LLC is:

- Epitome | serving as an excellent model, a perfect example
- Confident | positive, assured, self reliant
- Fresh | novel, revitalized
- Outstanding | notable, impressive
- Successful | doing well, profitable

There is a logo (that hopefully I can upload herein!) that must be used, but we are completely open to creative interpretation of the look and feel of the flyer. The flyer will be printed on high-quality stock paper and reviewed together with a prospective agent. The flyer will also be sent electronically.

Many thanks for your consideration! We are excited to see your approach!

Reason: Hello, everyone. I'm so sorry for the unexpected delay in a decision, but the client has requested just a little more time due to a personal matter. We cannot convey enough our appreciation for everyone's contributions, and we are very sorry for this unexpected, and unavoidable, delay. Please stand by. We hope to respond back to all by next Wednesday. Many thanks for your understanding and patience. Dalia

Real Estate

• We must have the logo in the design; as well as contact information as follows:

Quillstone Realty, LLC
4862 Maplewend Blvd., Suite 305
Brentwood, TN 37999
615.555.0187
www.quillstonerealtyhq.example

```html
<!DOCTYPE html>
<html lang="en">
<head>
<meta charset="utf-8">
<title>Quillstone Realty, LLC — Agent Flyer</title>
<link rel="stylesheet" href="https://fonts.googleapis.com/css2?family=Nothing+You+Could+Do&family=Delius&family=Arimo&display=swap">
<style>
  :root {
    --red-bright: #d11f45;
    --red-deep: #a51b2c;
    --red-dark: #8e1424;
    --black: #0b0b0b;
    --gold-light: #fbe9a0;
    --gold: #d3ac2b;
    --gold-dark: #9c7814;
    --white: #ffffff;
    --sky: #8fb8e0;
    --sky-pale: #d8e6f2;
    --water: #8fa1ac;
  }
  html, body {
    margin: 0;
    padding: 0;
    overflow: hidden;
    background: #ffffff;
  }
  .flyer {
    position: relative;
    width: 927px;
    height: 1200px;
    overflow: hidden;
  }
  .flyer-art {
    position: absolute;
    inset: 0;
    width: 927px;
    height: 1200px;
    display: block;
  }
  .tagline {
    position: absolute;
    margin: 0;
    font-family: "Nothing You Could Do", cursive;
    font-weight: 400;
    color: var(--white);
    font-size: 46px;
    line-height: 1;
  }
  .tagline span { position: absolute; white-space: nowrap; }
  .tagline .word-response   { left: 131px; top: 252px; }
  .tagline .word-innovative { left: 234px; top: 322px; }
  .tagline .word-deliver    { left: 196px; top: 392px; }

  .brand-name {
    position: absolute;
    left: 120px;
    top: 1006px;
    margin: 0;
    font-family: "Delius", sans-serif;
    font-weight: 400;
    font-size: 38px;
    color: var(--white);
    white-space: nowrap;
  }
  .contact {
    position: absolute;
    left: 131px;
    top: 1084px;
    margin: 0;
    font-family: "Delius", sans-serif;
    font-style: normal;
    font-size: 18px;
    line-height: 23px;
    color: var(--white);
  }
  .website {
    position: absolute;
    left: 507px;
    top: 1154px;
    margin: 0;
    font-family: "Arimo", sans-serif;
    font-size: 15px;
    color: var(--white);
  }
</style>
</head>
<body>
<main class="flyer">
  <svg class="flyer-art" viewBox="0 0 850 1100" preserveAspectRatio="none" aria-hidden="false">
    <defs>
      <linearGradient id="redField" x1="0" y1="0" x2="1" y2="1">
        <stop offset="0" stop-color="var(--red-bright)"/>
        <stop offset="0.55" stop-color="var(--red-deep)"/>
        <stop offset="1" stop-color="var(--red-dark)"/>
      </linearGradient>
      <linearGradient id="goldBar" x1="0" y1="0" x2="1" y2="0">
        <stop offset="0" stop-color="var(--gold-dark)"/>
        <stop offset="0.5" stop-color="var(--gold-light)"/>
        <stop offset="1" stop-color="var(--gold)"/>
      </linearGradient>
      <linearGradient id="goldStripe" x1="0" y1="0" x2="1" y2="1">
        <stop offset="0" stop-color="var(--gold)"/>
        <stop offset="0.5" stop-color="var(--gold-light)"/>
        <stop offset="1" stop-color="var(--gold-dark)"/>
      </linearGradient>
      <linearGradient id="skylineTone" x1="0" y1="0" x2="0" y2="1">
        <stop offset="0" stop-color="var(--sky)"/>
        <stop offset="0.5" stop-color="var(--sky-pale)"/>
        <stop offset="1" stop-color="var(--water)"/>
      </linearGradient>
    </defs>

    <rect class="red-field" x="0" y="0" width="850" height="1100" fill="url(#redField)"/>

    <g class="tagline-column">
      <rect x="80" y="0" width="318" height="620" fill="var(--black)"/>
      <rect x="96" y="0" width="14" height="620" fill="url(#goldBar)"/>
      <rect x="367" y="0" width="14" height="620" fill="url(#goldBar)"/>
    </g>

    <g class="skyline-photo" role="img" aria-label="Photo of a waterfront city skyline with high-rise towers under a blue sky">
      <polygon points="0,545 850,232 850,590 0,850" fill="url(#skylineTone)"/>
    </g>

    <polygon class="band-black" points="0,850 850,590 850,622 0,885" fill="var(--black)"/>
    <polygon class="band-white" points="0,885 850,622 850,650 0,935" fill="var(--white)"/>

    <g class="contact-panel">
      <polygon points="0,935 292,837 850,1072 850,1100 0,1100" fill="var(--black)"/>
      <polygon points="272,858 292,852 850,1086 850,1098" fill="url(#goldStripe)"/>
    </g>
  </svg>

  <h2 class="tagline">
    <span class="word-response">Response</span>
    <span class="word-innovative">Innovative</span>
    <span class="word-deliver">Deliver</span>
  </h2>

  <h1 class="brand-name">Quillstone Realty</h1>

  <address class="contact">
    Quillstone Realty, LLC<br>
    4862 Maplewend Blvd., Suite 305<br>
    Brentwood, TN 37999<br>
    615.555.0187
  </address>

  <p class="website">www.quillstonerealtyhq.example</p>
</main>
</body>
</html>
```